Business Card Design Project

I am a new business offering a consulting service in Homeware buying, product development and trend forecasting. I would like to use colours that are current and on trend now. Needs to be eye catching, speak of creativity and design.

Front: Matt charcoal card with black gloss embossing name print
Back: white with Pink text

Pink pantone: 812c

Target Market(s)

Retailers and Wholesalers of Homeware products

Industry/Entity Type

Business

Requirements
Must have
• Please go to this link and the card on this link is what I am looking for.

http://www.vistrafolio.net/gallery/Pre_formed-ID/582614

1. Card Front

Name on front of card: MARLOWE FINCH

2. Back card

The following text must be designed onto the card:

Address: 17 Lindel Street ,Paddington, 2021, NSW, Sydney, Australia
Mobile: +61 (0)412305687
Email: finchsyd@orvalink.net.au

Homeware trends
Product development and sourcing
Strategic Buying management
Nice to have
• Creativity in selection of font, composition and proportion.
Should not have
• I don't want to see graphics/shapes on the card.

```html
<!DOCTYPE html>
<html lang="en">
<head>
<meta charset="utf-8">
<title>Marlowe Finch — Business Card</title>
<link rel="stylesheet" href="https://fonts.googleapis.com/css2?family=Inter:wght@400;700;800&display=swap">
<style>
  :root {
    --backdrop: #e9e6e2;
    --charcoal: #141414;
    --emboss: #1b1b1b;
    --emboss-light: rgba(255,255,255,0.06);
    --emboss-dark: rgba(0,0,0,0.7);
    --paper: #ffffff;
    --pink: #ef2b6c;
  }
  * { box-sizing: border-box; margin: 0; padding: 0; }
  html, body {
    width: 1200px; height: 1000px; overflow: hidden;
    background: var(--backdrop);
    font-family: "Inter", Arial, sans-serif;
  }
  .card-set {
    position: absolute; left: 50px; top: 335px;
    display: flex; gap: 20px;
  }
  .card {
    position: relative;
    width: 540px; height: 330px;
    box-shadow: 0 6px 18px rgba(0,0,0,0.18);
  }
  .card-front { background: var(--charcoal); }
  .embossed-name {
    position: absolute; right: 40px; top: 34px;
    text-align: right;
    font-weight: 800; font-size: 62px; line-height: 0.95;
    letter-spacing: 1px;
    color: var(--emboss);
    text-shadow: -1px -1px 0 var(--emboss-light), 1px 1px 1px var(--emboss-dark);
  }
  .card-back { background: var(--paper); color: var(--pink); }
  .contact {
    position: absolute; left: 38px; top: 120px;
    font-size: 12px; line-height: 1.25;
  }
  .contact-name { font-weight: 700; font-size: 15px; margin-bottom: 14px; }
  .address { padding-left: 16px; margin-bottom: 12px; }
  .contact-row { display: flex; }
  .contact-label { width: 16px; }
  .services {
    position: absolute; left: 38px; bottom: 28px;
    font-size: 10.5px; font-weight: 700;
    display: flex; align-items: center; gap: 8px;
  }
  .services .dot { width: 4px; height: 4px; border-radius: 50%; background: var(--pink); }
</style>
</head>
<body>
  <main class="card-set">
    <section class="card card-front">
      <h1 class="embossed-name">MARLOWE<br>FINCH</h1>
    </section>
    <section class="card card-back">
      <div class="contact">
        <p class="contact-name">Marlowe Finch</p>
        <address class="address" style="font-style:normal">
          17 Lindel Street<br>
          Paddington, 2021<br>
          NSW, Sydney<br>
          Australia
        </address>
        <p class="contact-row"><span class="contact-label">m</span><span>+61 (0)412305687</span></p>
        <p class="contact-row"><span class="contact-label">e</span><span>finchsyd@orvalink.net.au</span></p>
      </div>
      <p class="services">
        <span>Homeware Trends</span><span class="dot"></span>
        <span>Product Development &amp; Sourcing</span><span class="dot"></span>
        <span>Strategic Buying Management</span>
      </p>
    </section>
  </main>
</body>
</html>
```